Brambles Softball Tournaments Website Design

Our client would like us to design a website. The company is similar to Field Crest USA (https://fieldcrestusa.example).

We prefer Adobe Fonts in the design. Lorem ipsum is fine to use for content, except for headers. Please keep track of any images used in your design. We plan on purchasing the images used.

Number of Pages Required

1 page

Font styles to use
Sans Serif

Colors
0054AA
0677BA
7BADD7
CADEEF
E8F1F8

```html
<!DOCTYPE html>
<html lang="en">
<head>
<meta charset="utf-8">
<title>Brambles Softball Tournaments</title>
<link href="https://fonts.googleapis.com/css2?family=Bebas+Neue&family=Barlow+Condensed:wght@400;500;600;700&display=swap" rel="stylesheet">
<style>
:root{
  --blue:#0054AA;
  --blue-bright:#0677BA;
  --sky:#7BADD7;
  --ice:#CADEEF;
  --mist:#E8F1F8;
  --navy:#0b2146;
  --navy-deep:#071733;
  --navy-mid:#123266;
  --white:#ffffff;
  --ball:#f2e21a;
  --line:rgba(202,222,239,.22);
}
*{box-sizing:border-box;margin:0;padding:0}
html,body{width:1200px;height:4679px;overflow:hidden;background:var(--navy)}
body{font-family:"Barlow Condensed",Arial Narrow,sans-serif;color:var(--white)}
.page{position:relative;width:1200px;height:4679px;overflow:hidden;background:var(--navy)}
.abs{position:absolute}
.display{font-family:"Bebas Neue",Impact,sans-serif;font-weight:400;letter-spacing:1px;line-height:.9}
.body-copy{font-size:12px;line-height:1.45;color:var(--ice)}
.accent-rule{border-left:2px solid var(--sky);padding-left:14px}
.btn{position:absolute;display:flex;align-items:center;justify-content:center;border-radius:20px;font-size:9px;font-weight:700;letter-spacing:.5px;text-transform:uppercase;white-space:nowrap}
.btn-white{background:var(--white);color:var(--navy)}
.btn-outline{border:1.5px solid var(--white);color:var(--white)}
.btn-accent{background:var(--blue-bright);color:var(--white)}
.photo{position:absolute;overflow:hidden}

/* top bar & nav */
.topbar{left:0;top:0;width:1200px;height:36px;background:var(--blue)}
.topbar span{position:absolute;top:11px;font-size:10px;font-weight:600;letter-spacing:1px;color:var(--mist)}
.icon-dot{position:absolute;width:20px;height:20px;border-radius:50%;background:rgba(7,23,51,.35);display:flex;align-items:center;justify-content:center}
.nav a{position:absolute;top:70px;font-size:11px;font-weight:600;color:var(--white);text-decoration:none;text-transform:uppercase;letter-spacing:.5px}
.nav-line{position:absolute;top:109px;height:1px;background:var(--line)}
.brand{position:absolute;left:527px;top:0;width:146px;height:138px}
.brand-name{position:absolute;left:0;width:146px;top:36px;text-align:center;font-family:"Bebas Neue",sans-serif;font-size:26px;line-height:.95;color:var(--white)}

/* hero */
.hero-bg{left:0;top:0;width:1200px;height:944px;background:radial-gradient(ellipse at 50% 28%,#2b5c96 0%,#153a70 40%,var(--navy) 78%)}
.hero-kicker{left:0;width:1200px;top:166px;text-align:center;font-size:64px}
.hero-title{left:0;width:1200px;top:234px;text-align:center;font-size:112px}
.badge-ring{position:absolute;width:164px;height:164px;border-radius:50%;border:1px solid var(--line);display:flex;align-items:center;justify-content:center}

/* events */
.card{position:absolute;top:1922px;width:394px;height:314px}
.card-label{position:absolute;left:24px;bottom:26px;padding-left:12px;border-left:2px solid var(--white);font-size:18px;font-weight:600;text-transform:uppercase}
.card-arrow{position:absolute;right:22px;bottom:22px;width:34px;height:34px;border-radius:50%;background:var(--white);display:flex;align-items:center;justify-content:center}
.outline-word{font-family:"Bebas Neue",sans-serif;color:transparent;-webkit-text-stroke:1.5px rgba(202,222,239,.4);letter-spacing:4px;white-space:nowrap}

/* footer */
.foot-head{position:absolute;font-family:"Bebas Neue",sans-serif;font-size:26px;text-align:center;width:240px;letter-spacing:1px}
.foot-links{position:absolute;width:240px;text-align:center;list-style:none;font-size:11px;line-height:22px;color:var(--ice)}
.contact-icon{position:absolute;width:50px;height:50px;border-radius:50%;background:var(--blue);display:flex;align-items:center;justify-content:center}
.contact-text{position:absolute;font-size:11px;line-height:18px;color:var(--ice)}
.partner{position:absolute;top:3893px;width:180px;height:70px;border-radius:8px;background:rgba(18,50,102,.55);display:flex;align-items:center;justify-content:center}
</style>
</head>
<body>
<div class="page">

  <!-- HERO -->
  <div class="abs hero-bg"></div>
  <div class="photo" role="img" aria-label="Stadium crowd with raised arms, blurred under night lights" style="left:0;top:150px;width:1200px;height:760px;background:radial-gradient(ellipse at 20% 60%,rgba(123,173,215,.22),transparent 45%),radial-gradient(ellipse at 80% 55%,rgba(123,173,215,.18),transparent 45%),linear-gradient(180deg,rgba(6,119,186,.2),rgba(11,33,70,0) 75%)"></div>
  <div class="abs" style="left:369px;top:390px;width:460px;height:460px;border-radius:50%;background:radial-gradient(circle,var(--blue-bright) 0%,var(--blue) 55%,rgba(0,84,170,.25) 100%)"></div>
  <div class="photo" role="img" aria-label="Softball batter in helmet and team jersey, ready to swing" style="left:430px;top:300px;width:340px;height:560px;border-radius:170px 170px 0 0;background:linear-gradient(180deg,#3f7fc0 0%,var(--blue-bright) 40%,var(--blue) 75%,#08356b 100%)"></div>
  <div class="photo" role="img" aria-label="Yellow softball" style="left:510px;top:726px;width:180px;height:180px;border-radius:50%;background:radial-gradient(circle at 40% 38%,#fff57a,var(--ball) 65%,#bfae00);border:6px solid var(--navy-deep)"></div>

  <div class="abs display hero-kicker">Weekend Events</div>
  <div class="abs display hero-title">Lifelong Memories</div>
  <div class="abs" style="left:914px;top:308px;width:84px;height:84px;border-radius:50%;background:var(--blue-bright);display:flex;align-items:center;justify-content:center">
    <svg width="30" height="16" viewBox="0 0 30 16"><path d="M2 13 L26 4 M19 2 L27 4 L23 11" stroke="#fff" stroke-width="1.6" fill="none"/></svg>
  </div>
  <p class="abs body-copy accent-rule" style="left:196px;top:432px;width:240px">Lorem Ipsum is simply dummy text of the printing and typesetting industry. Lorem Ipsum has been the industry's standard dummy text ever since the 1500s</p>

  <div class="badge-ring" style="left:41px;top:653px"><svg width="104" height="84" role="img" aria-label="Event badge"><circle cx="52" cy="42" r="34" fill="var(--blue)" stroke="#fff" stroke-width="3"/><rect x="8" y="34" width="88" height="18" rx="3" fill="#fff"/></svg></div>
  <div class="badge-ring" style="left:238px;top:729px"><svg width="100" height="84" role="img" aria-label="Event badge"><polygon points="50,6 88,30 80,72 20,72 12,30" fill="#2d4c7c" stroke="var(--ice)" stroke-width="2.5"/><rect x="14" y="40" width="72" height="14" fill="var(--ice)"/></svg></div>
  <div class="badge-ring" style="left:796px;top:729px"><svg width="100" height="84" role="img" aria-label="Event badge"><polygon points="50,6 90,28 90,58 50,78 10,58 10,28" fill="var(--blue)" stroke="#fff" stroke-width="2.5"/><circle cx="50" cy="42" r="16" fill="var(--sky)"/></svg></div>
  <div class="badge-ring" style="left:996px;top:657px"><svg width="100" height="90" role="img" aria-label="Event badge"><polygon points="50,4 62,34 94,36 68,56 78,88 50,70 22,88 32,56 6,36 38,34" fill="var(--blue-bright)" stroke="#fff" stroke-width="2.5"/></svg></div>

  <!-- TOP BAR / NAV -->
  <div class="abs topbar">
    <div class="icon-dot" style="left:150px;top:8px"><svg width="10" height="10" viewBox="0 0 10 10"><path d="M2 1 L4 1 L5 3 L4 4 Q5 6 6 6 L7 5 L9 6 L9 8 Q8 9 7 9 Q1 8 1 3 Q1 2 2 1Z" fill="#fff"/></svg></div>
    <span style="left:186px">+1 555 014 2290</span>
    <span style="left:790px">INFO@BRAMBLESSOFTBALL.EXAMPLE</span>
    <div class="icon-dot" style="left:975px;top:8px"><svg width="10" height="8" viewBox="0 0 18 13"><rect x="1" y="1" width="16" height="11" fill="#fff"/></svg></div>
    <div class="icon-dot" style="left:1030px;top:8px"><svg width="10" height="10" viewBox="0 0 10 10"><circle cx="5" cy="3" r="2.2" fill="#fff"/><path d="M1 10 Q5 4 9 10Z" fill="#fff"/></svg></div>
  </div>
  <div class="brand">
    <svg width="146" height="138" viewBox="0 0 146 138"><path d="M8 6 H138 V78 Q138 112 73 136 Q8 112 8 78Z" fill="var(--navy-deep)" stroke="var(--blue-bright)" stroke-width="5"/></svg>
    <div class="brand-name">Brambles<br>Softball</div>
  </div>
  <nav class="nav">
    <a style="left:149px">About Us</a>
    <a style="left:241px">Baseball</a>
    <a style="left:336px">Soft Ball</a>
    <a style="left:432px">Hotels</a>
    <a style="left:732px">Fan Shop</a>
  </nav>
  <div class="nav-line" style="left:149px;width:338px"></div>
  <div class="nav-line" style="left:683px;width:370px"></div>
  <div class="btn btn-outline" style="left:846px;top:62px;width:98px;height:28px">Info Packet</div>
  <div class="btn btn-white" style="left:955px;top:62px;width:96px;height:28px">Nomination</div>

  <!-- PRICELESS -->
  <div class="abs" style="left:196px;top:1020px;width:363px;height:420px;background:var(--blue-bright)"></div>
  <div class="photo" role="img" aria-label="Excited fans cheering in the stands" style="left:196px;top:1004px;width:363px;height:443px;clip-path:polygon(0 0,88% 0,100% 4%,100% 100%,6% 100%,0 96%);background:radial-gradient(ellipse at 45% 60%,#d6a98a 0%,#9c6a58 35%,#3f5a84 75%,#1e3c6e 100%)"></div>
  <div class="abs display" style="left:608px;top:1026px;font-size:34px">Your Weekends Are</div>
  <div class="abs display" style="left:608px;top:1072px;font-size:100px">Priceless</div>
  <div class="abs accent-rule body-copy" style="left:608px;top:1186px;width:395px">
    <p>Lorem Ipsum is simply dummy text of the printing and typesetting industry. Lorem Ipsum has been the industry's standard dummy text ever since the 1500s, when an unknown printer took a galley of type and scrambled it to make a type specimen book. It has survived not only five centuries, but also the leap into electronic typesetting, remaining essentially unchanged.</p>
    <p style="margin-top:16px">Lorem Ipsum is simply dummy text of the printing and typesetting industry. Lorem Ipsum has been the industry's standard dummy text ever since the 1500s, when an unknown printer took a galley of type and scrambled it to make a type specimen book.</p>
  </div>
  <div class="btn btn-white" style="left:608px;top:1387px;width:133px;height:30px">More About Us</div>

  <!-- EVENTS BAND -->
  <svg class="abs" style="left:0;top:1480px" width="1200" height="645" viewBox="0 0 1200 645">
    <defs><linearGradient id="bandGrad" x1="0" y1="0" x2="0" y2="1"><stop offset="0" stop-color="#0677BA"/><stop offset="1" stop-color="#0054AA"/></linearGradient></defs>
    <path d="M0 5 L600 118 L1200 5 V640 H0Z" fill="url(#bandGrad)"/>
    <path d="M540 30 L600 70 L660 30 M525 45 L600 95 L675 45" stroke="rgba(232,241,248,.6)" stroke-width="2" fill="none"/>
  </svg>
  <div class="abs display" style="left:196px;top:1654px;font-size:34px">With Over</div>
  <div class="abs display" style="left:196px;top:1700px;font-size:100px">150 Events Annually</div>
  <div class="abs accent-rule" style="left:196px;top:1820px;width:400px;border-color:var(--white);font-size:16px;font-weight:600;line-height:1.4;text-transform:uppercase">And in business since 2005, we're more than just tournaments.</div>
  <div class="btn btn-outline" style="left:773px;top:1834px;width:111px;height:28px">Baseball</div>
  <div class="btn btn-white" style="left:891px;top:1834px;width:111px;height:28px;color:var(--blue)">Softball</div>

  <div class="abs display outline-word" style="left:0;width:1200px;top:2196px;text-align:center;font-size:112px">Softball Tournaments</div>

  <div class="card photo" role="img" aria-label="Team huddled together on the field" style="left:196px;background:linear-gradient(180deg,#a9bccf 0%,#6f8a86 40%,#2f4a3e 70%,#0f1b2a 100%)">
    <div class="card-label">Team Events</div>
    <div class="card-arrow"><svg width="16" height="10"><path d="M1 5 H14 M10 1 L14 5 L10 9" stroke="#0054AA" stroke-width="1.5" fill="none"/></svg></div>
  </div>
  <div class="card photo" role="img" aria-label="Athlete sprinting on a stadium track" style="left:610px;background:linear-gradient(180deg,#cadeef 0%,#8fa8bf 40%,#56657a 70%,#141d2a 100%)">
    <div class="card-label">Individual Events</div>
    <div class="card-arrow"><svg width="16" height="10"><path d="M1 5 H14 M10 1 L14 5 L10 9" stroke="#0054AA" stroke-width="1.5" fill="none"/></svg></div>
  </div>

  <!-- HOW IT WORKS -->
  <div class="photo" role="img" aria-label="Baseball stadium at night from above" style="left:0;top:2330px;width:1200px;height:680px;background:radial-gradient(ellipse at 50% 58%,#2c6a5a 0%,#1c4a6e 22%,#14356a 50%,var(--navy) 82%)"></div>
  <div class="abs display" style="left:0;width:1200px;text-align:center;top:2402px;font-size:34px">How It</div>
  <div class="abs display" style="left:0;width:1200px;text-align:center;top:2446px;font-size:100px">Works</div>

  <svg class="abs" style="left:0;top:2540px" width="1200" height="450" viewBox="0 2540 1200 450" font-family="Bebas Neue, sans-serif">
    <g fill="#0054AA" opacity=".7">
      <polygon points="351,2871 398,2789 494,2789 541,2871 494,2953 398,2953"/>
      <polygon points="656,2871 703,2789 799,2789 846,2871 799,2953 703,2953"/>
      <polygon points="260,2630 280,2596 318,2596 338,2630 318,2664 280,2664"/>
      <polygon points="930,2576 950,2545 988,2545 1008,2576 988,2607 950,2607"/>
      <polygon points="296,2880 312,2854 340,2854 356,2880 340,2906 312,2906"/>
    </g>
    <g fill="#ffffff" stroke="rgba(7,23,51,.3)" stroke-width="2">
      <polygon points="197,2762 244,2680 340,2680 387,2762 340,2844 244,2844"/>
      <polygon points="351,2653 398,2571 494,2571 541,2653 494,2735 398,2735"/>
      <polygon points="504,2762 551,2680 647,2680 694,2762 647,2844 551,2844"/>
      <polygon points="656,2653 703,2571 799,2571 846,2653 799,2735 703,2735"/>
      <polygon points="811,2762 858,2680 954,2680 1001,2762 954,2844 858,2844"/>
    </g>
    <g fill="none" stroke="#7BADD7" stroke-width="1" font-size="30" text-anchor="middle">
      <text x="292" y="2742">01</text><text x="446" y="2633">02</text><text x="599" y="2742">03</text><text x="751" y="2633">04</text><text x="906" y="2742">05</text>
    </g>
    <g fill="#0054AA">
      <rect x="279" y="2750" width="26" height="22" rx="2"/><rect x="283" y="2758" width="18" height="11" fill="#fff"/>
      <path d="M432 2644 H438 L442 2660 H458 L462 2648 H440" stroke="#0054AA" stroke-width="3" fill="none"/><circle cx="444" cy="2667" r="3"/><circle cx="456" cy="2667" r="3"/>
      <circle cx="599" cy="2753" r="5"/><circle cx="589" cy="2757" r="4"/><circle cx="609" cy="2757" r="4"/><path d="M584 2774 Q599 2756 614 2774Z"/>
      <rect x="740" y="2644" width="22" height="24"/><rect x="745" y="2650" width="4" height="4" fill="#fff"/><rect x="753" y="2650" width="4" height="4" fill="#fff"/><rect x="749" y="2660" width="5" height="8" fill="#fff"/>
      <circle cx="906" cy="2762" r="13"/><path d="M897 2753 Q906 2762 897 2771 M915 2753 Q906 2762 915 2771" stroke="#fff" stroke-width="1.5" fill="none"/>
    </g>
    <g fill="#0b2146" font-family="Barlow Condensed, sans-serif" font-weight="700" font-size="17" text-anchor="middle">
      <text x="292" y="2820">SCHEDULE</text><text x="446" y="2711">CHECKOUT</text><text x="599" y="2820">ROSTER</text><text x="751" y="2711">HOTEL</text><text x="906" y="2820">PLAY</text>
    </g>
  </svg>

  <!-- INFO PACKET -->
  <svg class="abs" style="left:0;top:2990px" width="1200" height="260" viewBox="0 0 1200 260"><polygon points="0,0 1200,130 1200,260 0,260" fill="#081a3a"/></svg>
  <div class="abs" style="left:0;top:3250px;width:1200px;height:800px;background:#081a3a"></div>
  <div class="abs outline-word" style="left:640px;top:3080px;font-size:130px;transform:rotate(14deg);transform-origin:left top;-webkit-text-stroke:1.5px rgba(202,222,239,.55)">Info Packet</div>
  <div class="photo" role="img" aria-label="Tournament flyer poster with softball and event date" style="left:440px;top:3290px;width:420px;height:300px;transform:rotate(-20deg);background:linear-gradient(135deg,#12203a 0%,#243a5e 50%,#7BADD7 85%,#CADEEF 100%);box-shadow:0 20px 40px rgba(0,0,0,.5)"></div>
  <div class="abs display" style="left:196px;top:3212px;font-size:34px">Download Our</div>
  <div class="abs display" style="left:196px;top:3258px;font-size:100px;line-height:.97">Free Info<br>Packet</div>
  <p class="abs body-copy accent-rule" style="left:196px;top:3544px;width:240px">Lorem Ipsum is simply dummy text of the printing and typesetting industry. Lorem Ipsum has been the industry's standard dummy text ever since the 1500s</p>
  <div class="btn btn-accent" style="left:196px;top:3640px;width:152px;height:28px">Request the Info Packet</div>

  <div class="abs" style="left:196px;top:3765px;width:806px;height:1px;background:var(--line)"></div>
  <div class="partner" role="img" aria-label="Partner badge" style="left:231px"><svg width="120" height="34"><circle cx="17" cy="17" r="15" fill="var(--blue-bright)"/><rect x="40" y="10" width="78" height="14" rx="3" fill="var(--sky)"/></svg></div>
  <div class="partner" role="img" aria-label="Partner badge" style="left:509px"><svg width="120" height="34"><rect x="2" y="10" width="92" height="14" rx="3" fill="var(--ice)"/><circle cx="108" cy="17" r="10" fill="var(--blue-bright)"/></svg></div>
  <div class="partner" role="img" aria-label="Partner badge" style="left:785px"><svg width="120" height="34"><rect x="6" y="4" width="108" height="16" rx="3" fill="var(--sky)"/><rect x="22" y="24" width="76" height="6" rx="2" fill="var(--blue-bright)"/></svg></div>

  <!-- FOOTER -->
  <svg class="abs" style="left:0;top:4010px" width="1200" height="669" viewBox="0 0 1200 669"><path d="M0 40 Q600 -20 1200 40 V669 H0Z" fill="var(--navy-deep)"/></svg>
  <div class="abs" style="left:1076px;top:3957px;width:80px;height:80px;border-radius:50%;border:1px solid var(--line);display:flex;align-items:center;justify-content:center">
    <svg width="24" height="18"><path d="M2 10 L12 2 L22 10 M2 16 L12 8 L22 16" stroke="#fff" stroke-width="1.5" fill="none"/></svg>
  </div>
  <div class="abs" style="left:1116px;top:4037px;width:1px;height:60px;background:var(--line)"></div>

  <div class="brand" style="top:4090px;left:504px;width:192px;height:182px">
    <svg width="192" height="182" viewBox="0 0 146 138"><path d="M8 6 H138 V78 Q138 112 73 136 Q8 112 8 78Z" fill="var(--navy-deep)" stroke="var(--blue-bright)" stroke-width="4"/></svg>
    <div class="brand-name" style="width:192px;top:50px;font-size:33px">Brambles<br>Softball</div>
  </div>

  <div class="foot-head" style="left:185px;top:4182px">Quicklinks</div>
  <ul class="foot-links" style="left:185px;top:4228px">
    <li>Home</li><li>About Us</li><li>Team Hotels</li><li>Individual Hotels</li><li>Fan Shop</li><li>Info Packet</li><li>Nomination</li><li>Careers/Jobs</li><li>Sign In - Team</li><li>Sign In - Individual</li>
  </ul>
  <div class="abs" style="left:436px;top:4220px;width:1px;height:228px;background:var(--line)"></div>
  <div class="foot-head" style="left:479px;top:4302px">Softball</div>
  <ul class="foot-links" style="left:479px;top:4351px">
    <li>Team</li><li>Individual</li><li>Rules</li><li>All-Star Weekend</li><li>Prospect Team</li>
  </ul>
  <div class="abs" style="left:755px;top:4220px;width:1px;height:228px;background:var(--line)"></div>
  <div class="foot-head" style="left:789px;top:4182px">Baseball</div>
  <ul class="foot-links" style="left:789px;top:4230px">
    <li>Team</li><li>Individual</li><li>Rules</li><li>Junior All-American Games</li><li>Pre-Season Championships</li><li>Silver Series Championships</li><li>National Championships</li><li>All-Star Weekend</li><li>Prospect Team</li>
  </ul>

  <div class="abs" role="img" aria-label="Social profile" style="left:562px;top:4497px;width:16px;height:16px;border-radius:50%;background:var(--mist)"></div>
  <div class="abs" role="img" aria-label="Social profile" style="left:591px;top:4497px;width:16px;height:16px;border-radius:50%;background:var(--mist)"></div>
  <div class="abs" role="img" aria-label="Social profile" style="left:620px;top:4497px;width:16px;height:16px;border-radius:50%;background:var(--mist)"></div>

  <div class="contact-icon" style="left:233px;top:4549px"><svg width="16" height="16" viewBox="0 0 10 10"><path d="M2 1 L4 1 L5 3 L4 4 Q5 6 6 6 L7 5 L9 6 L9 8 Q8 9 7 9 Q1 8 1 3 Q1 2 2 1Z" fill="#fff"/></svg></div>
  <div class="contact-text" style="left:302px;top:4565px">+1 555 014 2290</div>
  <div class="contact-icon" style="left:503px;top:4549px"><svg width="14" height="18" viewBox="0 0 14 18"><path d="M7 17 Q1 9 1 6 A6 6 0 0 1 13 6 Q13 9 7 17Z" fill="#fff"/><circle cx="7" cy="6" r="2.2" fill="#0054AA"/></svg></div>
  <div class="contact-text" style="left:566px;top:4556px">PO Box 4120<br>Cedar Falls, IL 60000</div>
  <div class="contact-icon" style="left:777px;top:4549px"><svg width="18" height="13" viewBox="0 0 18 13"><rect x="1" y="1" width="16" height="11" fill="#fff"/><path d="M1 1 L9 7 L17 1" stroke="#0054AA" stroke-width="1.2" fill="none"/></svg></div>
  <div class="contact-text" style="left:846px;top:4565px">info@bramblessoftball.example</div>

  <div class="abs" style="left:0;top:4624px;width:1200px;height:1px;background:var(--line)"></div>
  <div class="abs" style="left:0;top:4644px;width:1200px;text-align:center;font-size:11px;color:var(--ice)">Copyright © 2023 BRAMBLES SOFTBALL. All rights reserved.</div>
  <div class="abs" style="left:0;top:4673px;width:1200px;height:6px;background:var(--blue)"></div>
</div>
</body>
</html>
```